Wordpress website for voluntary transgender support online

We need a website as an information support for transgender people and their friends and families. We are a self funded voluntary support group reaching out to educate all in need.
Fairly basic site. Tabs for 3 of us to put bios, professional resources and contacts, news, general information, our contact info, entertainment.
Our logo is attached and we'd love the use of clouds and the colour lilac. We wish to look professional but approachable and personable.

Target Market(s)

Transgender people,mr heir families and friends and general public.

Industry/Entity Type

Group

Requirements
Must have
• Willow 4 logo.
• Tabs for: about us, contacts, news, bios x3, suggestions, professional resources, entertainment, personal resources, general information.
• We are hoping to set up in Wordpress so that we can then manage the page and update in the future.
• Coding will be required.
Nice to have
• Any suggestions.

```html
<!DOCTYPE html>
<html lang="en">
<head>
<meta charset="utf-8">
<title>Willow 4 – Transgender Support</title>
<link rel="stylesheet" href="https://fonts.googleapis.com/css2?family=Lato:wght@300;400;700;900&family=Open+Sans:wght@400;600;700&display=swap">
<style>
:root{
  --purple:#5a3988;
  --purple-deep:#3f2466;
  --lilac:#8f70bf;
  --lilac-soft:#b9a5d9;
  --ink:#333340;
  --muted:#7a7a86;
  --line:#e3e0ea;
  --sky-top:#3f6fb0;
  --sky-low:#a9c5e6;
  --night:#241c2e;
  --night-deep:#17121e;
  --white:#ffffff;
}
*{box-sizing:border-box;margin:0;padding:0}
html,body{width:1200px;height:2868px;overflow:hidden}
body{font-family:"Open Sans",Arial,sans-serif;color:var(--ink);background:var(--white);position:relative}
.page{position:relative;width:1200px;height:2868px;overflow:hidden}

/* header */
.site-header{position:absolute;top:0;left:0;width:1200px;height:88px;background:var(--white);z-index:3}
.brand{position:absolute;left:130px;top:14px;display:flex;align-items:center;gap:10px}
.brand-dot{width:22px;height:22px;border-radius:50%;background:var(--lilac)}
.brand-name{font-family:"Lato",sans-serif;font-weight:700;font-size:34px;color:var(--purple);letter-spacing:.5px}
.brand-tag{position:absolute;left:162px;top:56px;font-size:9px;letter-spacing:2px;color:var(--muted);text-transform:uppercase}
.top-phone{position:absolute;right:130px;top:6px;font-size:13px;color:var(--purple);display:flex;align-items:center;gap:6px}
.main-nav{position:absolute;right:130px;top:44px;display:flex;gap:4px}
.main-nav a{font-family:"Lato",sans-serif;font-size:12px;font-weight:700;color:var(--muted);text-decoration:none;padding:9px 16px;letter-spacing:.5px}
.main-nav a.current{background:var(--purple);color:var(--white)}

/* hero */
.hero{position:absolute;top:88px;left:0;width:1200px;height:480px;background:linear-gradient(180deg,var(--sky-top) 0%,#6f97cc 55%,var(--sky-low) 100%);overflow:hidden}
.hero-figure{position:absolute;left:640px;top:0;width:240px;height:450px;background:linear-gradient(180deg,#5b4338 0%,#2a2330 45%,#1d1a22 100%);border-radius:110px 110px 10px 10px}
.hero-copy{position:absolute;left:195px;top:105px;color:var(--white)}
.hero-title{font-family:"Lato",sans-serif;font-weight:300;font-size:72px;line-height:72px;letter-spacing:1px}
.hero-text{margin-top:18px;width:400px;font-size:13px;line-height:19px}
.btn-ghost{display:inline-block;margin-top:26px;border:1px solid var(--white);color:var(--white);font-size:10px;font-weight:700;padding:9px 18px;letter-spacing:.5px}
.hero-clouds{position:absolute;left:0;bottom:0;width:1200px;height:120px}

/* section titles */
.section-title{font-family:"Lato",sans-serif;font-weight:700;font-size:22px;color:var(--purple);text-align:center;letter-spacing:1px}
.section-title::after{content:"";display:block;width:60px;height:2px;background:var(--lilac);margin:10px auto 0}
.section-intro{width:940px;margin:18px auto 0;font-size:12px;line-height:20px;color:var(--muted);text-align:center}

/* who we are */
.who{position:absolute;top:568px;left:0;width:1200px;height:380px;background:linear-gradient(180deg,#fff 0%,#f3f1f7 100%)}
.who .section-title{margin-top:12px}
.features{display:flex;justify-content:center;gap:140px;margin-top:50px}
.feature{width:220px;text-align:center}
.feature-icon{width:64px;height:64px;margin:0 auto}
.feature h3{font-family:"Lato",sans-serif;font-size:13px;color:var(--purple);margin-top:12px;letter-spacing:.5px}
.feature p{font-size:11px;color:var(--muted);line-height:17px;margin-top:6px}
.who-edge{position:absolute;left:0;bottom:-40px;width:1200px;height:80px}

/* news */
.news{position:absolute;top:1030px;left:0;width:1200px;height:520px}
.card-row{display:flex;justify-content:center;gap:26px;margin-top:34px}
.news-card{width:290px}
.card-photo{position:relative;height:150px}
.date-badge{position:absolute;left:0;top:0;width:42px;height:46px;background:var(--purple);color:var(--white);text-align:center;font-family:"Lato",sans-serif}
.date-badge b{display:block;font-size:18px;padding-top:5px}
.date-badge span{font-size:9px}
.card-title{font-family:"Lato",sans-serif;font-weight:700;font-size:13px;color:var(--purple);margin-top:16px}
.card-meta{margin-top:12px;font-size:11px;color:var(--muted);line-height:24px;border-top:1px solid var(--line);padding-top:6px}
.card-meta div{display:flex;align-items:center;gap:8px;border-bottom:1px solid var(--line)}
.meta-dot{width:9px;height:9px;background:var(--lilac-soft)}
.card-link{display:block;margin-top:10px;font-size:11px;color:var(--purple);font-weight:600}

/* blog */
.blog{position:absolute;top:1580px;left:0;width:1200px;height:470px}
.blog-band{position:absolute;inset:0;width:1200px;height:470px}
.blog-inner{position:absolute;top:20px;left:0;width:1200px;color:var(--white)}
.blog .section-title{color:var(--white)}
.blog .section-title::after{background:var(--white)}
.blog .section-intro{color:#e4dcf1}
.blog-row{display:flex;justify-content:center;gap:14px;margin-top:30px}
.blog-card{width:222px;background:var(--white);color:var(--ink)}
.blog-card .card-photo{height:140px}
.blog-meta{font-size:10px;color:var(--muted);padding:6px 10px;display:flex;justify-content:space-between;border-top:1px solid var(--line)}

/* help */
.help{position:absolute;top:2075px;left:0;width:1200px;height:380px}
.help-body{display:flex;gap:40px;margin:38px 0 0 195px}
.help-photo{width:360px;height:240px;background:linear-gradient(135deg,#d9d3cc 0%,#8a7b6f 50%,#2e2b33 100%)}
.help-text{width:420px;font-size:12px;line-height:20px;color:var(--muted)}
.help-text .card-link{margin-top:16px}

/* contact */
.contact{position:absolute;top:2455px;left:0;width:1200px;height:305px;background:var(--night)}
.contact-head{position:absolute;left:0;top:0;width:1200px;height:60px}
.contact-label{position:absolute;left:0;top:10px;width:1200px;text-align:center;font-family:"Lato",sans-serif;font-weight:700;font-size:20px;color:var(--white);letter-spacing:1px}
.contact-info{position:absolute;left:195px;top:90px;color:#cfc8da;font-size:12px;line-height:30px}
.contact-info div{display:flex;align-items:center;gap:10px}
.contact-form{position:absolute;left:610px;top:90px;width:395px}
.field-row{display:flex;gap:10px}
.field{flex:1;height:30px;border:1px solid #4a4056;color:#9a90a8;font-size:11px;padding:7px 10px;margin-bottom:10px}
.field.message{height:80px}
.btn-submit{background:var(--purple);color:var(--white);text-align:center;font-family:"Lato",sans-serif;font-weight:700;font-size:14px;padding:12px 0;letter-spacing:1px}

.site-footer{position:absolute;top:2760px;left:0;width:1200px;height:108px;background:var(--night-deep)}
.social{position:absolute;left:170px;top:40px;display:flex;gap:12px}
.social span{width:22px;height:22px;background:#4a4056}
.social span:first-child{background:var(--white)}
.copyright{position:absolute;right:170px;top:44px;font-size:11px;color:#8a8196}
</style>
</head>
<body>
<div class="page">

<header class="site-header">
  <div class="brand"><span class="brand-dot"></span><span class="brand-name">Willow 4</span></div>
  <div class="brand-tag">Transgender Support</div>
  <div class="top-phone">
    <svg width="12" height="12" viewBox="0 0 24 24"><path d="M6.6 10.8a15 15 0 0 0 6.6 6.6l2.2-2.2a1 1 0 0 1 1-.25 11.4 11.4 0 0 0 3.6.6 1 1 0 0 1 1 1V20a1 1 0 0 1-1 1A17 17 0 0 1 3 4a1 1 0 0 1 1-1h3.5a1 1 0 0 1 1 1c0 1.25.2 2.45.6 3.6a1 1 0 0 1-.25 1z" fill="#5a3988"/></svg>
    123.456.7890
  </div>
  <nav class="main-nav">
    <a class="current" href="#">HOME</a><a href="#">ABOUT US</a><a href="#">OUR SERVICES</a><a href="#">CONTACT US</a>
  </nav>
</header>

<section class="hero">
  <div class="hero-figure" role="img" aria-label="Photo of a smiling woman in a dark dress standing against the sky"></div>
  <div class="hero-copy">
    <h1 class="hero-title">SUPPORT<br>TRASNGENDER</h1>
    <p class="hero-text">We offer kind, private and friendly help for people who are finding their way, and for the families and friends who love them.</p>
    <span class="btn-ghost">READ MORE</span>
  </div>
  <svg class="hero-clouds" viewBox="0 0 1200 120" preserveAspectRatio="none" aria-hidden="true">
    <path d="M0 120 V80 C60 60 110 70 150 85 C190 50 260 50 300 80 C340 45 420 40 460 75 C500 40 570 30 610 70 C650 35 730 35 770 72 C810 45 880 45 920 78 C960 50 1040 50 1080 80 C1120 62 1170 64 1200 75 V120 Z" fill="#ffffff"/>
  </svg>
</section>

<section class="who">
  <h2 class="section-title">WHO WE ARE</h2>
  <p class="section-intro">We are a small, self funded volunteer group. We share clear information, trusted resources and a warm ear for transgender people, their partners, parents and friends. Whatever stage you are at, you are welcome here and you are never alone.</p>
  <div class="features">
    <div class="feature">
      <svg class="feature-icon" viewBox="0 0 64 64"><circle cx="32" cy="32" r="30" fill="#5a3988"/><circle cx="29" cy="35" r="9" fill="none" stroke="#fff" stroke-width="3"/><path d="M35 29 L44 20 M38 20 H44 V26" fill="none" stroke="#fff" stroke-width="3"/></svg>
      <h3>TRANS GENDER</h3>
      <p>Plain facts and gentle guidance for every step of your journey.</p>
    </div>
    <div class="feature">
      <svg class="feature-icon" viewBox="0 0 64 64"><circle cx="32" cy="32" r="30" fill="#e3dcee"/><path d="M20 42 V24 L32 34 L44 24 V42" fill="none" stroke="#8f70bf" stroke-width="3"/></svg>
      <h3>HELP &amp; SUPPORT</h3>
      <p>Someone to talk to, links to experts and a safe place to ask.</p>
    </div>
    <div class="feature">
      <svg class="feature-icon" viewBox="0 0 64 64"><circle cx="32" cy="32" r="30" fill="#e3dcee"/><circle cx="32" cy="26" r="7" fill="none" stroke="#8f70bf" stroke-width="3"/><path d="M20 46 C22 36 42 36 44 46" fill="none" stroke="#8f70bf" stroke-width="3"/></svg>
      <h3>VOLUNTEERING</h3>
      <p>Join our team and give a little time to help others feel heard.</p>
    </div>
  </div>
  <svg class="who-edge" viewBox="0 0 1200 80" preserveAspectRatio="none" aria-hidden="true"><path d="M0 40 Q600 80 1200 40 V0 H0 Z" fill="#f3f1f7"/></svg>
</section>

<section class="news">
  <h2 class="section-title">OUR NEWS</h2>
  <p class="section-intro">Catch up with the latest from our group: meetups, events, useful updates and stories shared by members of our community across the region.</p>
  <div class="card-row">
    <article class="news-card">
      <div class="card-photo" role="img" aria-label="Photo of a person outdoors in warm light" style="background:linear-gradient(135deg,#c9a98d,#6d5446)"><div class="date-badge"><b>28</b><span>MAY</span></div></div>
      <h3 class="card-title">MONTHLY MEETUP DATES ANNOUNCED</h3>
      <div class="card-meta"><div><span class="meta-dot"></span>Willow 4 Team</div><div><span class="meta-dot"></span>Posted in Community Events</div></div>
      <p class="card-meta" style="border:0">Our new calendar is ready with friendly evenings for all.</p>
      <span class="card-link">Continue Reading →</span>
    </article>
    <article class="news-card">
      <div class="card-photo" role="img" aria-label="Photo of a couple close together" style="background:linear-gradient(135deg,#8a7c84,#2e2a33)"><div class="date-badge"><b>21</b><span>MAY</span></div></div>
      <h3 class="card-title">A GUIDE FOR FAMILY MEMBERS</h3>
      <div class="card-meta"><div><span class="meta-dot"></span>Willow 4 Team</div><div><span class="meta-dot"></span>Posted in Family Resources</div></div>
      <p class="card-meta" style="border:0">Simple ways to listen, learn and stand by someone you love.</p>
      <span class="card-link">Continue Reading →</span>
    </article>
    <article class="news-card">
      <div class="card-photo" role="img" aria-label="Photo of a busy city street at dusk" style="background:linear-gradient(135deg,#b45a55,#3a3350)"><div class="date-badge"><b>14</b><span>MAY</span></div></div>
      <h3 class="card-title">PRIDE WALK THIS SUMMER</h3>
      <div class="card-meta"><div><span class="meta-dot"></span>Willow 4 Team</div><div><span class="meta-dot"></span>Posted in Local News</div></div>
      <p class="card-meta" style="border:0">Walk with us and bring friends, family and good cheer.</p>
      <span class="card-link">Continue Reading →</span>
    </article>
  </div>
</section>

<section class="blog">
  <svg class="blog-band" viewBox="0 0 1200 470" preserveAspectRatio="none" role="img" aria-label="Deep purple band with a softly blurred city photo">
    <defs><linearGradient id="band" x1="0" y1="0" x2="1" y2="1"><stop offset="0" stop-color="#3f2466"/><stop offset="1" stop-color="#5a3988"/></linearGradient></defs>
    <path d="M0 40 L600 0 L1200 40 V430 L600 470 L0 430 Z" fill="url(#band)"/>
  </svg>
  <div class="blog-inner">
    <h2 class="section-title">OUR BLOG</h2>
    <p class="section-intro">Personal stories, honest advice and a little entertainment from the three of us and our guests. Read, share and join the conversation.</p>
    <div class="blog-row">
      <article class="blog-card"><div class="card-photo" role="img" aria-label="Photo of friends talking" style="background:linear-gradient(135deg,#a39486,#4a3f3a)"><div class="date-badge"><b>02</b><span>JUN</span></div></div><div class="blog-meta"><span>Willow 4</span><span>3 Comments</span></div></article>
      <article class="blog-card"><div class="card-photo" role="img" aria-label="Photo of a group at a table" style="background:linear-gradient(135deg,#d8c7b4,#7c6a5c)"><div class="date-badge"><b>29</b><span>MAY</span></div></div><div class="blog-meta"><span>Willow 4</span><span>5 Comments</span></div></article>
      <article class="blog-card"><div class="card-photo" role="img" aria-label="Photo of a person in sunglasses" style="background:linear-gradient(135deg,#e6d2b8,#9b7560)"><div class="date-badge"><b>24</b><span>MAY</span></div></div><div class="blog-meta"><span>Willow 4</span><span>2 Comments</span></div></article>
      <article class="blog-card"><div class="card-photo" role="img" aria-label="Photo of a city skyline at sunset" style="background:linear-gradient(180deg,#e8a25c,#6b4a7a)"><div class="date-badge"><b>18</b><span>MAY</span></div></div><div class="blog-meta"><span>Willow 4</span><span>4 Comments</span></div></article>
    </div>
  </div>
</section>

<section class="help">
  <h2 class="section-title">HELP TO TRANS GENDER</h2>
  <div class="help-body">
    <div class="help-photo" role="img" aria-label="Photo of a smiling man and woman side by side"></div>
    <div class="help-text">
      <p>Coming out, changing a name or finding the right doctor can feel like a lot. We gather trusted professional resources, local services and personal guides in one calm place so you can find what you need quickly.</p>
      <p style="margin-top:12px">You can reach any of us by message, join a group evening or simply read at your own pace. Families and friends are just as welcome to ask questions, and every chat stays private and respectful.</p>
      <span class="card-link">Continue Reading →</span>
    </div>
  </div>
</section>

<section class="contact">
  <svg class="contact-head" viewBox="0 0 1200 60" preserveAspectRatio="none" aria-hidden="true"><path d="M0 0 H1200 V20 L600 50 L0 20 Z" fill="#5a3988"/></svg>
  <h2 class="contact-label">CONTACT</h2>
  <div class="contact-info">
    <div><svg width="12" height="14" viewBox="0 0 24 28"><path d="M12 0a10 10 0 0 0-10 10c0 7.5 10 18 10 18s10-10.5 10-18A10 10 0 0 0 12 0zm0 14a4 4 0 1 1 0-8 4 4 0 0 1 0 8z" fill="#b9a5d9"/></svg>48 Lantern Row, Brookvale, Eastshire</div>
    <div><svg width="12" height="12" viewBox="0 0 24 24"><path d="M6.6 10.8a15 15 0 0 0 6.6 6.6l2.2-2.2a1 1 0 0 1 1-.25 11.4 11.4 0 0 0 3.6.6 1 1 0 0 1 1 1V20a1 1 0 0 1-1 1A17 17 0 0 1 3 4a1 1 0 0 1 1-1h3.5a1 1 0 0 1 1 1c0 1.25.2 2.45.6 3.6a1 1 0 0 1-.25 1z" fill="#b9a5d9"/></svg>123.456.7890</div>
    <div><svg width="13" height="10" viewBox="0 0 26 20"><rect x="1" y="1" width="24" height="18" fill="none" stroke="#b9a5d9" stroke-width="2"/><path d="M1 1 L13 11 L25 1" fill="none" stroke="#b9a5d9" stroke-width="2"/></svg>hello@willow4group.org</div>
  </div>
  <div class="contact-form">
    <div class="field-row"><div class="field">Your Name</div><div class="field">Your Email</div></div>
    <div class="field message">Message</div>
    <div class="btn-submit">FIND OUT MORE</div>
  </div>
</section>

<footer class="site-footer">
  <div class="social"><span></span><span></span><span></span><span></span><span></span><span></span></div>
  <div class="copyright">© 2024 Willow 4 · All rights reserved</div>
</footer>

</div>
</body>
</html>
```